professional business card

A Clean looking business card for a money transfer company. Our company is call Velorix= Transfer + Send = Transcend (next level)
to show professionalism as well as some effects to show digital tech.

1 side to have position, name and address
2 side to have company name and show that we provide money exchange and cross-border money transfer

Target Market(s)

Remittance companies and high net worth individuals

Industry/Entity Type

Finance

Contact Information for Business Card

Name, address, email, title, services- money exchange and cross-border remittance

Requirements
Nice to have
• Digital age feel

```html
<!DOCTYPE html>
<html lang="en">
<head>
<meta charset="utf-8">
<title>Velorix Business Cards</title>
<link href="https://fonts.googleapis.com/css2?family=Montserrat:wght@500;600;700&display=swap" rel="stylesheet">
<style>
  :root {
    --board: #5f5f5f;
    --board-edge: #3f3f3f;
    --paper: #ffffff;
    --ink: #183342;
    --deep: #003140;
    --teal: #1ec8d8;
    --teal-soft: #8fd9df;
    --card-line: #8a8a8a;
  }
  * { box-sizing: border-box; margin: 0; padding: 0; }
  html, body {
    width: 1200px; height: 753px; overflow: hidden;
    background: var(--board);
    font-family: "Montserrat", Arial, sans-serif;
  }
  .artboard {
    position: relative; width: 1200px; height: 753px;
    border-top: 2px solid var(--board-edge);
  }
  .card {
    position: absolute; width: 518px; height: 289px; overflow: hidden;
    border: 1px solid var(--card-line);
  }
  .card--light { background: var(--paper); color: var(--ink); }
  .card--dark { background: var(--deep); color: var(--paper); }
  .card--front-light { left: 35px; top: 56px; }
  .card--back-light { left: 644px; top: 56px; border-color: #222; }
  .card--front-dark { left: 35px; top: 401px; }
  .card--back-dark { left: 644px; top: 401px; }

  /* digital circuit decoration areas */
  .circuit {
    position: absolute; top: 0; height: 100%;
  }
  .circuit--left {
    left: 0; width: 150px;
    background: linear-gradient(90deg, rgba(143,217,223,0.55), rgba(143,217,223,0));
  }
  .circuit--right {
    right: 0; width: 150px;
    background: linear-gradient(270deg, rgba(143,217,223,0.55), rgba(143,217,223,0));
  }
  .card--dark .circuit--left {
    background: linear-gradient(90deg, rgba(30,200,216,0.35), rgba(30,200,216,0));
  }
  .card--dark .circuit--right {
    background: linear-gradient(270deg, rgba(30,200,216,0.35), rgba(30,200,216,0));
  }
  .transfer-icon {
    position: absolute; left: 418px; top: 12px; width: 88px; height: 87px;
    border-radius: 8px;
    background: radial-gradient(circle, rgba(30,200,216,0.55), rgba(143,217,223,0.15));
  }

  .brand {
    position: absolute; left: 117px; top: 122px;
    display: flex; align-items: center; gap: 12px;
  }
  .brand__dot {
    width: 40px; height: 40px; border-radius: 50%;
    background: var(--teal);
  }
  .brand__name {
    font-size: 37px; font-weight: 600; letter-spacing: 0.5px;
    line-height: 44px; text-transform: uppercase;
  }

  .contact {
    position: absolute; left: 34px; top: 0; width: 470px; height: 100%;
  }
  .contact__title {
    position: absolute; top: 38px;
    font-size: 20px; font-weight: 600; letter-spacing: 0.6px;
  }
  .contact__address {
    position: absolute; top: 94px;
    font-size: 20px; font-weight: 600; line-height: 25px; letter-spacing: 0.6px;
  }
  .contact__email {
    position: absolute; top: 184px;
    font-size: 20px; font-weight: 600; letter-spacing: 0.3px;
  }
  .contact__services {
    position: absolute; left: -4px; top: 247px;
    font-size: 14.5px; font-weight: 700; letter-spacing: 0;
    text-transform: uppercase; white-space: nowrap;
  }
</style>
</head>
<body>
<main class="artboard">

  <section class="card card--light card--front-light">
    <div class="circuit circuit--left" role="img" aria-label="Digital circuit trace pattern in light teal"></div>
    <div class="transfer-icon" role="img" aria-label="Money transfer icon with globe and exchange arrows"></div>
    <div class="brand">
      <span class="brand__dot"></span>
      <span class="brand__name">Velorix</span>
    </div>
  </section>

  <section class="card card--light card--back-light">
    <div class="circuit circuit--right" role="img" aria-label="Digital circuit trace pattern in light teal"></div>
    <div class="contact">
      <p class="contact__title">John Doe - CEO</p>
      <p class="contact__address">MY ADDRESS HERE, 1001<br>MY ADDRESS HERE, 1001</p>
      <p class="contact__email">johndoe.ceo@velorix.com</p>
      <p class="contact__services">Money exchange and cross-border remittance</p>
    </div>
  </section>

  <section class="card card--dark card--front-dark">
    <div class="circuit circuit--left" role="img" aria-label="Digital circuit trace pattern in teal"></div>
    <div class="transfer-icon" role="img" aria-label="Money transfer icon with globe and exchange arrows"></div>
    <div class="brand">
      <span class="brand__dot"></span>
      <span class="brand__name">Velorix</span>
    </div>
  </section>

  <section class="card card--dark card--back-dark">
    <div class="circuit circuit--right" role="img" aria-label="Digital circuit trace pattern in teal"></div>
    <div class="contact">
      <p class="contact__title">John Doe - CEO</p>
      <p class="contact__address">MY ADDRESS HERE, 1001<br>MY ADDRESS HERE, 1001</p>
      <p class="contact__email">johndoe.ceo@velorix.com</p>
      <p class="contact__services">Money exchange and cross-border remittance</p>
    </div>
  </section>

</main>
</body>
</html>
```